Kelvo Rinn Computing Group - Need a Sales Promotion Flyer for a Managed IT Services company

We need a 4x9 (Front/Back) promotional sales flyer for a IT Consulting / Managed IT Services company.

Tailor the design after the uploaded logo and website screenshot.

Target Market(s)

Local Small Businesses

Industry/Entity Type

Information Technology

Other font styles liked:
• Sansation

Requirements
Must have
• Front of Flyer (Content):
• - Logo & Phone #
• - Tag Line: Your Local Technology Business Partner (Main Focus)
• - Text: Free IT Assessment (Main Focus)
• - Contact Information (Bottom)
• - Phone: 555.218.7391
• - Email: info@kelvorinnco.com
• - Web: www.kelvorinnco.com
• - Address: 482 N. Harlow St. / Suite 214
• Brenmoor CA 95517
• Back of Flyer:
• - Business Solutions
• - Managed IT Services
• - IT Consulting
• - About Us (Bottom)
• - Trusted Technology Partner
• - Client First
• - Industry Experts
• - Professional Staff
• - Latest Technologies
• Based in the beautiful Brenmoor Valley surrounded by the Corvane Ridge mountains, Kelvo Rinn Computing Group is a trusted technology partner providing a wide range of business solutions, IT services, cloud services and IT consulting.

```html
<!DOCTYPE html>
<html lang="en">
<head>
<meta charset="utf-8">
<title>Kelvo Rinn Computing Group – Flyer</title>
<link href="https://fonts.googleapis.com/css2?family=Oswald:wght@500;600;700&family=Titillium+Web:wght@400;600;700;900&display=swap" rel="stylesheet">
<style>
:root{
  --stage:#2b2b2b;
  --navy:#2d2a7a;
  --navy-deep:#152447;
  --orange:#f7941d;
  --plum:#7b1f4e;
  --brown:#6b5b45;
  --text-dark:#3a1a1a;
  --bold-red:#6a0f18;
  --tag-red:#9b1b1f;
  --green:#9bc13c;
  --red:#ea3128;
  --dark-red:#8c1a1a;
  --yellow:#f2e600;
  --lime:#d7df23;
  --gold:#e6c85a;
  --white:#ffffff;
  --purple:#7b2b8c;
  --gear-blue:#25408f;
  --gear-yellow:#f6a81c;
  --gear-green:#a5cd39;
  --gear-pink:#e43a8d;
  --gear-sky:#2a75bb;
}
*{margin:0;padding:0;box-sizing:border-box}
html,body{width:1200px;height:1200px;overflow:hidden;background:var(--stage)}
body{position:relative;font-family:"Titillium Web",sans-serif}
.flyer{position:absolute;background:var(--white);overflow:hidden}
.flyer--back{left:82px;top:132px;width:436px;height:960px}
.flyer--front{left:657px;top:120px;width:494px;height:974px}
.band{position:absolute;left:0;width:100%;display:flex;align-items:center;justify-content:center;text-align:center}
.heading{font-family:"Oswald",sans-serif;font-weight:600;color:var(--white);text-transform:uppercase}

/* back */
.back-title{top:0;height:58px;background:var(--navy);font-size:29px;letter-spacing:-.3px;font-weight:700}
.brand{position:absolute;left:0;width:100%;text-align:center;font-family:"Titillium Web",sans-serif;font-weight:700;color:var(--brown);line-height:1.02}
.brand--back{top:108px;font-size:44px}
.section-head{height:50px;background:var(--orange);font-size:28px}
.services{position:absolute;top:324px;left:0;width:100%;height:184px;display:flex;justify-content:space-around;align-items:center;padding:0 8px}
.service{width:130px;height:130px;border-radius:50%;border:15px solid;display:flex;align-items:center;justify-content:center;text-align:center;font-family:"Oswald",sans-serif;font-weight:500;font-size:16px;line-height:1.45;color:var(--white);text-transform:uppercase}
.service--managed{background:var(--gear-blue);border-color:var(--purple)}
.service--business{background:var(--gear-green);border-color:var(--gear-yellow)}
.service--consulting{background:var(--gear-sky);border-color:var(--gear-pink)}
.copy{position:absolute;left:24px;right:24px;text-align:center;font-size:16.5px;line-height:22px;color:var(--text-dark)}
.copy b{color:var(--bold-red);font-weight:700}
.values{position:absolute;top:676px;left:0;width:100%;height:102px;display:grid;grid-template-columns:1fr 1fr}
.value{display:flex;align-items:center;justify-content:center;font-family:"Oswald",sans-serif;font-weight:500;font-size:16px;color:var(--white);text-transform:uppercase}
.value--orange{background:var(--orange)}
.value--plum{background:var(--plum)}
.web{font-weight:700;font-size:25px;gap:14px;letter-spacing:-.3px}
.back-web{top:908px;height:52px;background:var(--navy);color:var(--white)}

/* front */
.brand--front{top:36px;font-size:52px}
.tagline{top:196px;height:34px;background:var(--tag-red);color:var(--yellow);font-size:20px;font-weight:600}
.call{top:230px;height:58px;background:var(--green);gap:20px;font-family:"Oswald",sans-serif;font-weight:500;color:var(--white);font-size:32px}
.photo{position:absolute;top:288px;left:0;width:100%;height:306px;background:radial-gradient(ellipse at 50% 45%,#5a6482 0%,#2e3550 45%,#1e2438 80%),#2e3550}
.offer{top:594px;height:104px;background:var(--navy-deep)}
.offer span{font-family:"Oswald",sans-serif;font-weight:700;font-size:56px;color:var(--gold);letter-spacing:-.5px;text-transform:uppercase}
.book{position:absolute;top:698px;left:0;width:247px;height:220px;background:var(--red);text-align:center;padding-top:6px}
.book p{font-weight:700;color:var(--white);font-size:27px;line-height:36px}
.book p:first-child{font-weight:400}
.book .cta{color:var(--yellow);font-size:26px;line-height:27px}
.contact{position:absolute;top:698px;left:247px;width:247px;height:181px;background:var(--dark-red);color:var(--white);padding:8px 0 0 22px}
.contact h3{font-family:"Oswald",sans-serif;font-weight:500;font-size:27px;color:var(--lime);text-align:center;margin-left:-22px;line-height:1.2}
.contact .rule{height:2px;background:var(--gear-sky);width:198px;margin:8px 0 14px 0}
.line{display:flex;gap:10px;font-size:14px;line-height:20px}
.line svg{flex:none;margin-top:2px}
.phone-strip{position:absolute;top:879px;left:247px;width:247px;height:39px;background:var(--green);display:flex;align-items:center;justify-content:center;gap:14px;font-family:"Oswald",sans-serif;font-weight:500;font-size:28px;color:var(--white)}
.front-web{top:918px;height:56px;background:var(--lime);color:#111}
</style>
</head>
<body>

<section class="flyer flyer--back">
  <div class="band heading back-title">Kelvo Rinn Computing Group</div>
  <div class="brand brand--back">Kelvo Rinn<br>Computing Group</div>
  <div class="band heading section-head" style="top:274px">Our Services</div>
  <div class="services">
    <div class="service service--managed">Managed<br>IT Services</div>
    <div class="service service--business">Business<br>Solutions</div>
    <div class="service service--consulting">IT<br>Consulting</div>
  </div>
  <div class="band heading section-head" style="top:508px">About Us</div>
  <p class="copy" style="top:568px">We will help you connect your business with the <b>latest technologies using a comprehensive set of IT services and business solutions</b> to improve business performance and IT agility.</p>
  <div class="values">
    <div class="value value--orange">Trusted Technology Partner</div>
    <div class="value value--plum">Client First</div>
    <div class="value value--plum">Industry Experts</div>
    <div class="value value--orange">Professional Staff</div>
  </div>
  <p class="copy" style="top:786px;left:10px;right:10px">Based in the beautiful Brenmoor Valley surrounded by the Corvane Ridge mountains, Kelvo Rinn Computing Group is a trusted technology partner providing a wide range of business solutions, IT services, cloud services and IT consulting.</p>
  <div class="band web back-web">
    <svg width="32" height="32" viewBox="0 0 32 32" fill="none" stroke="#c9a27a" stroke-width="1.6"><circle cx="16" cy="16" r="14"/><ellipse cx="16" cy="16" rx="6" ry="14"/><line x1="2" y1="16" x2="30" y2="16"/><line x1="5" y1="9" x2="27" y2="9"/><line x1="5" y1="23" x2="27" y2="23"/></svg>
    <span>www.kelvorinnco.com</span>
  </div>
</section>

<section class="flyer flyer--front">
  <div class="brand brand--front">Kelvo Rinn<br>Computing Group</div>
  <div class="band tagline heading">Your Local Technology Business Partner</div>
  <div class="band call">
    <span>CALL US</span>
    <svg width="44" height="44" viewBox="0 0 44 44" fill="none" stroke="#111" stroke-width="3"><circle cx="22" cy="22" r="19"/><path d="M15 12c-2 2-2 6 1 11s8 9 12 9c2 0 3-1 4-2l-4-4-3 2c-2-1-5-4-6-6l2-3-4-4z" fill="#111" stroke="none"/></svg>
    <span>555-218-7391</span>
  </div>
  <div class="photo" role="img" aria-label="Photo of a consultant in a suit holding his hands around the word Consulting, surrounded by small business icons"></div>
  <div class="band offer"><span>Free IT Assessment</span></div>
  <div class="book">
    <p>To Book Your</p>
    <p>FREE Technology Assessment</p>
    <p class="cta">Visit Our Website</p>
    <p class="cta">or</p>
    <p class="cta">Call Us Today</p>
  </div>
  <div class="contact">
    <h3>CONTACT US</h3>
    <div class="rule"></div>
    <div class="line">
      <svg width="16" height="20" viewBox="0 0 16 20"><path d="M8 0a7 7 0 0 0-7 7c0 5 7 13 7 13s7-8 7-13a7 7 0 0 0-7-7z" fill="#b5c93a"/><circle cx="8" cy="7" r="2.5" fill="#8c1a1a"/></svg>
      <span>ADDRESS<br>482 N. Harlow St. / Suite 214<br>Brenmoor CA 95517</span>
    </div>
    <div class="line" style="margin-top:14px">
      <svg width="18" height="18" viewBox="0 0 18 18"><circle cx="9" cy="9" r="9" fill="#2a9fd8"/><path d="M6 12l6-6M7 8l-2 2a2 2 0 0 0 3 3l2-2M11 10l2-2a2 2 0 0 0-3-3L8 7" stroke="#fff" stroke-width="1.4" fill="none"/></svg>
      <span>info@kelvorinnco.com</span>
    </div>
  </div>
  <div class="phone-strip">
    <svg width="28" height="28" viewBox="0 0 44 44" fill="none" stroke="#111" stroke-width="3"><circle cx="22" cy="22" r="19"/><path d="M15 12c-2 2-2 6 1 11s8 9 12 9c2 0 3-1 4-2l-4-4-3 2c-2-1-5-4-6-6l2-3-4-4z" fill="#111" stroke="none"/></svg>
    <span>555-218-7391</span>
  </div>
  <div class="band web front-web">
    <svg width="36" height="36" viewBox="0 0 32 32" fill="none" stroke="#111" stroke-width="1.8"><circle cx="16" cy="16" r="14"/><ellipse cx="16" cy="16" rx="6" ry="14"/><line x1="2" y1="16" x2="30" y2="16"/><line x1="5" y1="9" x2="27" y2="9"/><line x1="5" y1="23" x2="27" y2="23"/></svg>
    <span>www.kelvorinnco.com</span>
  </div>
</section>

</body>
</html>
```